Ebook cover for a Wild edible plant book

We are looking for an ebook cover for a wild edible plant book about California. The title is Hillside Forage Guide of California. The subtitle is Gather, Sort, Dry, and Season Your Fresh Hillside Harvest Greens. The author's name is Marla Quentin. Please bring original ideas to the table, as we will not be considering anything replicating something from a book already available on Brindle.

```html
<!DOCTYPE html>
<html lang="en">
<head>
<meta charset="utf-8">
<title>Hillside Forage Guide of California — Cover</title>
<link rel="stylesheet" href="https://fonts.googleapis.com/css2?family=Montserrat:wght@500;800&family=Oswald:wght@600;700&family=Poppins:wght@400&display=swap">
<style>
  :root {
    --stage: #eeeeee;
    --paper: #ffffff;
    --ink-dark: #333333;
    --leaf-green: #2f7d1e;
    --pill-green: #2e6e1c;
    --title-red: #d2161c;
    --sub-ink: #2a2a2a;
  }
  * { box-sizing: border-box; margin: 0; padding: 0; }
  html, body {
    width: 1179px; height: 1200px; overflow: hidden;
    background: var(--stage);
  }
  .cover {
    position: absolute; left: 215px; top: 40px;
    width: 750px; height: 1120px;
    background: var(--paper);
    display: flex; flex-direction: column;
  }
  .photo-row {
    display: grid; grid-template-columns: repeat(3, 1fr);
    gap: 8px; height: 305px;
  }
  .photo { width: 100%; height: 100%; }
  .photo--coast-house { background: linear-gradient(160deg, #4f9be0 0%, #cfe4f4 45%, #b84fa8 46%, #6b8a4c 70%, #e9e9e4 100%); }
  .photo--sea-succulents { background: linear-gradient(180deg, #3d7fa3 0%, #5c8d8f 40%, #c9b52c 65%, #b4461e 85%, #3e5a2a 100%); }
  .photo--potted-seedling { background: linear-gradient(170deg, #6c6a64 0%, #4f7d2e 35%, #c47a56 60%, #3a2a22 100%); }
  .photo--agave-bloom { background: linear-gradient(180deg, #2f4a2c 0%, #6a8a5a 50%, #a7b7a0 75%, #3e5232 100%); }
  .photo--rosette-succulent { background: linear-gradient(180deg, #9aa79a 0%, #5a4a52 40%, #8fc4c8 75%, #e0cdbd 100%); }
  .photo--purple-sage { background: linear-gradient(180deg, #5f6f3a 0%, #6a3a8c 40%, #7a4b9e 65%, #4f6a36 100%); }

  .title-block {
    flex: 1;
    display: flex; flex-direction: column; align-items: center;
    padding-top: 26px;
  }
  .title-lead {
    font-family: "Montserrat", sans-serif; font-weight: 800;
    font-size: 56px; line-height: 1; color: var(--ink-dark);
    letter-spacing: 0.5px;
  }
  .title-main {
    font-family: "Oswald", sans-serif; font-weight: 700;
    font-size: 190px; line-height: 0.95; color: var(--leaf-green);
    letter-spacing: -1px; margin-top: 2px;
  }
  .title-region {
    font-family: "Montserrat", sans-serif; font-weight: 500;
    font-size: 52px; line-height: 1; color: var(--title-red);
    margin-top: 4px;
  }
  .subtitle {
    font-family: "Poppins", sans-serif; font-weight: 400;
    font-size: 21px; line-height: 1.45; color: var(--sub-ink);
    text-align: center; margin-top: 18px;
  }
  .byline {
    position: relative; margin-top: 20px;
    display: flex; align-items: center; gap: 10px;
  }
  .sprig {
    width: 130px; height: 30px; border-radius: 15px;
    background: linear-gradient(90deg, rgba(106,140,70,0) 0%, #7d9a5c 60%, #5e7f3e 100%);
  }
  .sprig--right { transform: scaleX(-1); }
  .author-pill {
    background: var(--pill-green); color: var(--paper);
    font-family: "Oswald", sans-serif; font-weight: 600;
    font-size: 33px; letter-spacing: 0.5px;
    padding: 2px 30px 4px; border-radius: 10px; line-height: 1.4;
  }
</style>
</head>
<body>
  <main class="cover">
    <section class="photo-row photo-row--top">
      <div class="photo photo--coast-house" role="img" aria-label="Photo of a white coastal house with flowering bougainvillea under a blue sky"></div>
      <div class="photo photo--sea-succulents" role="img" aria-label="Photo of yellow and red succulents by the sea"></div>
      <div class="photo photo--potted-seedling" role="img" aria-label="Photo of hands placing a seedling in a terracotta pot"></div>
    </section>

    <section class="title-block">
      <h1 class="title">
        <span class="title-lead" style="display:block;text-align:center">HILLSIDE FORAGE</span>
        <span class="title-main" style="display:block;text-align:center">GUIDE</span>
        <span class="title-region" style="display:block;text-align:center">OF CALIFORNIA</span>
      </h1>
      <p class="subtitle">Gather, Sort, Dry, and Season Your Fresh<br>Hillside Harvest Greens.</p>
      <div class="byline">
        <div class="sprig" role="img" aria-label="Green herb sprig ornament"></div>
        <span class="author-pill">MARLA QUENTIN</span>
        <div class="sprig sprig--right" role="img" aria-label="Green herb sprig ornament"></div>
      </div>
    </section>

    <section class="photo-row photo-row--bottom">
      <div class="photo photo--agave-bloom" role="img" aria-label="Photo of a spiky plant with a purple bloom"></div>
      <div class="photo photo--rosette-succulent" role="img" aria-label="Photo of a dark rosette succulent among pale succulents"></div>
      <div class="photo photo--purple-sage" role="img" aria-label="Photo of purple sage flowers"></div>
    </section>
  </main>
</body>
</html>
```